Boat business cards

I'm looking for business cards with the two logos I've attached. I don't have an specific idea in mind and open to anything. All the usual info will be on the card. Name, position in company, nr, email, address, ect. The company rents out these two boats for charters and fishing.

```html
<!DOCTYPE html>
<html lang="en">
<head>
<meta charset="UTF-8">
<title>Tide &amp; Star Charters — Business Card</title>
<link href="https://fonts.googleapis.com/css2?family=Poppins:wght@400;500;600&display=swap" rel="stylesheet">
<style>
  :root{
    --backdrop:#1d6890;
    --card:#ffffff;
    --brand-blue:#3a9ad6;
    --ink:#2b2b2b;
    --ink-soft:#4a4a4a;
    --rule:#3c3c3c;
    --logo-grey:#5c6670;
  }
  *{margin:0;padding:0;box-sizing:border-box}
  html,body{width:1200px;height:1080px;overflow:hidden}
  body{background:var(--backdrop);font-family:'Poppins',sans-serif;position:relative}
  .card{position:absolute;left:160px;width:880px;height:490px;background:var(--card);
        box-shadow:0 10px 30px rgba(0,0,0,.25);overflow:hidden}
  .card--front{top:35px}
  .card--back{top:555px}

  .logo{position:absolute;display:flex;align-items:center;gap:12px;font-weight:600;font-size:44px;letter-spacing:1px}
  .logo__mark{width:22px;height:22px;border-radius:50%}
  .logo--tidewater{color:var(--logo-grey)}
  .logo--tidewater .logo__mark{background:var(--brand-blue)}
  .logo--harbor{color:var(--ink)}
  .logo--harbor .logo__mark{background:#a88a5c}

  .card--front .logo--tidewater{left:70px;top:95px}
  .card--front .logo--harbor{right:75px;top:200px}

  .divider{position:absolute;left:70px;right:150px;top:290px;height:2px;background:var(--rule)}

  .contact{position:absolute;left:55px;top:315px;list-style:none;font-size:17px;color:var(--ink-soft);line-height:30px}
  .contact li{display:flex;align-items:center;gap:10px}
  .contact svg{width:14px;height:14px;fill:var(--brand-blue)}

  .person{position:absolute;right:70px;top:305px;text-align:right}
  .person__name{font-size:27px;font-weight:600;color:var(--brand-blue);letter-spacing:1px;text-transform:uppercase}
  .person__role{font-size:19px;color:var(--ink-soft);margin-top:-4px}
  .person__address{font-size:16px;color:var(--ink-soft);line-height:24px;margin-top:14px}

  .tagline-band{position:absolute;left:0;right:0;bottom:0;height:58px;background:var(--brand-blue);
        display:flex;align-items:center;justify-content:center}
  .tagline{font-size:20px;color:#fff;text-transform:uppercase;letter-spacing:.5px}

  .card--back .logos{position:absolute;left:0;right:0;top:150px;display:flex;justify-content:center;gap:70px}
  .card--back .logo{position:static}
  .card--back .tagline{position:absolute;left:0;right:0;top:345px;text-align:center;color:var(--brand-blue);font-size:22px}
</style>
</head>
<body>
  <section class="card card--front">
    <div class="logo logo--tidewater"><span class="logo__mark"></span>Tidewater</div>
    <div class="logo logo--harbor"><span class="logo__mark"></span>Harbor Star</div>
    <div class="divider"></div>
    <ul class="contact">
      <li><svg viewBox="0 0 24 24"><path d="M6.6 10.8a15 15 0 0 0 6.6 6.6l2.2-2.2a1 1 0 0 1 1-.25 11.4 11.4 0 0 0 3.6.57 1 1 0 0 1 1 1V20a1 1 0 0 1-1 1A17 17 0 0 1 3 4a1 1 0 0 1 1-1h3.5a1 1 0 0 1 1 1c0 1.25.2 2.45.57 3.57a1 1 0 0 1-.25 1z"/></svg>555.210.347</li>
      <li><svg viewBox="0 0 24 24"><path d="M2 5h20v14H2z M2 5l10 8 10-8" /></svg>hello@tidestarcharters.com</li>
      <li><svg viewBox="0 0 24 24"><circle cx="12" cy="12" r="10"/></svg>www.tidestarcharters.com</li>
    </ul>
    <div class="person">
      <div class="person__name">Marco Reyes Lane</div>
      <div class="person__role">Broker/Owner</div>
      <div class="person__address">480 Marina Drive, Suite 3<br>Bayside Cove BC 2051</div>
    </div>
    <div class="tagline-band"><p class="tagline">We rent out these two boats for charters and fishing.</p></div>
  </section>

  <section class="card card--back">
    <div class="logos">
      <div class="logo logo--tidewater"><span class="logo__mark"></span>Tidewater</div>
      <div class="logo logo--harbor"><span class="logo__mark"></span>Harbor Star</div>
    </div>
    <p class="tagline">We rent out these two boats for charters and fishing.</p>
  </section>
</body>
</html>
```